Chiropractic healthcare group business card

We are a Portland Oregon based chiropractic healthcare group. Looking for a new business card design. Something cutting edge, that shows off our new logo and tag line.Use either of the attached logos.Our tag line = "Who would you be without pain?"I'm open to about anything, impress me!!
Target Market(s)
Chiropractic patients - Auto injury, back pain, sports injuries, neck , shoulder, hip, knee, ankle pain.
Industry/Entity Type
Chiropractic
Contact Information for Business Card
Dr. Bram Holtvick, D.C.
Clinic name - Fernway Chiropractic
2 clinics
location #1
20418 NW Marwick Road
Suite B
North Plains, OR 97133
Location #2
13529 SE Calloway Street
Portland OR 97236
Main phone line 971.555.0143
website : www.FernwayClinics.example
Tag line "Who would you be without pain?"
Colors
Designer to choose colors to be used in the design.
Requirements
Must have
- Use the logo colors -- Want the orange color to be a TRUE orange.
- Both clinic address
- phone number
- website
- personal email - b.holtvick@ReliefBeginsHere.example
- tag line - "Who would you be without pain?"

```html
<!DOCTYPE html>
<html lang="en">
<head>
<meta charset="utf-8">
<title>Fernway Chiropractic – Business Card</title>
<link rel="stylesheet" href="https://fonts.googleapis.com/css2?family=Source+Sans+3:wght@400;600;700&display=swap">
<style>
  :root {
    --orange: #e8761c;
    --charcoal: #545554;
    --paper: #eeeeee;
    --backdrop: #e0e0e0;
    --ink: #4a4a4a;
    --white: #ffffff;
  }
  * { box-sizing: border-box; margin: 0; padding: 0; }
  html, body {
    width: 1200px; height: 1021px; overflow: hidden;
    background: var(--backdrop);
    font-family: "Source Sans 3", sans-serif;
  }
  .card {
    position: absolute; left: 250px;
    width: 700px; height: 400px;
    box-shadow: 0 3px 10px rgba(0,0,0,0.18);
    overflow: hidden;
  }
  /* Back side */
  .card--back { top: 90px; background: var(--charcoal); }
  .back__brand {
    position: absolute; top: 150px; left: 0; width: 100%;
    display: flex; justify-content: center; align-items: center; gap: 14px;
    color: var(--orange); font-weight: 700; font-size: 40px; letter-spacing: 1px;
  }
  .brand-square { width: 18px; height: 18px; background: var(--orange); flex: none; }
  .tagline {
    position: absolute; top: 300px; width: 100%; text-align: center;
    color: var(--white); font-size: 17px; letter-spacing: 0.5px; text-transform: uppercase;
  }
  .tagline em { font-style: normal; color: var(--orange); }

  /* Front side */
  .card--front { top: 530px; background: var(--paper); }
  .front__band { position: absolute; inset: 0; }
  .front__brand {
    position: absolute; top: 52px; left: 40px;
    display: flex; align-items: center; gap: 12px;
    color: var(--ink); font-weight: 700; font-size: 30px; letter-spacing: 1px;
  }
  .front__brand .brand-square { width: 16px; height: 16px; }
  .person { position: absolute; top: 60px; right: 40px; text-align: right; }
  .person__name { color: var(--orange); font-weight: 700; font-size: 25px; }
  .person__role { color: var(--ink); font-size: 19px; margin-top: 2px; }
  .contact {
    position: absolute; top: 188px; left: 40px;
    color: var(--white); font-size: 17px; line-height: 1.3;
  }
  .contact__address { margin-bottom: 4px; }
  .contact__line { display: flex; align-items: center; gap: 8px; }
  .contact__line svg { width: 15px; height: 15px; flex: none; }
  .front__mark {
    position: absolute; top: 250px; right: 40px;
    color: var(--orange); font-weight: 700; font-size: 30px;
  }
  .website {
    position: absolute; bottom: 12px; right: 40px;
    color: var(--ink); font-size: 19px;
  }
  .website span { color: var(--orange); }
</style>
</head>
<body>
  <section class="card card--back">
    <div class="back__brand"><span class="brand-square"></span>Fernway Chiropractic</div>
    <p class="tagline">Who would you be <em>without pain?</em></p>
  </section>

  <section class="card card--front">
    <svg class="front__band" viewBox="0 0 700 400" preserveAspectRatio="none">
      <polygon points="0,165 700,165 700,335 385,335 360,378 0,378" fill="var(--charcoal)"/>
    </svg>

    <div class="front__brand"><span class="brand-square"></span>Fernway Chiropractic</div>

    <div class="person">
      <p class="person__name">Dr. Bram Holtvick, D.C.</p>
      <p class="person__role">Founder</p>
    </div>

    <div class="contact">
      <p class="contact__address">20418 NW Marwick Road, Suite B<br>North Plains, OR 97133</p>
      <p class="contact__address">13529 SE Calloway Street<br>Portland OR 97236</p>
      <p class="contact__line">
        <svg viewBox="0 0 16 16"><path d="M3 1h3l1.5 4-2 1.3a9 9 0 0 0 4.2 4.2L11 8.5l4 1.5v3a2 2 0 0 1-2 2A13 13 0 0 1 1 3a2 2 0 0 1 2-2z" fill="var(--orange)"/></svg>
        971.555.0143
      </p>
      <p class="contact__line">
        <svg viewBox="0 0 16 16"><rect x="1" y="3" width="14" height="10" fill="none" stroke="var(--orange)" stroke-width="1.6"/><path d="M1 3l7 6 7-6" fill="none" stroke="var(--orange)" stroke-width="1.6"/></svg>
        b.holtvick@ReliefBeginsHere.example
      </p>
    </div>

    <div class="front__mark">Fernway Chiropractic</div>

    <p class="website">www.<span>FernwayClinics</span>.example</p>
  </section>
</body>
</html>
```